Sparrowgate Petals Website v.1 - attract floral shop franchisees

I need a simple information website for my new business. We are a franchisor of flower shops. The overall purpose of the website is to promote the company and the service, especially to potential franchisees and retailers. Only about 4 pages are required including homepage, About, For Supermarkets, For Franchisees, and Contact. No special functions are required except the site will have two separate inquiry forms that must be filled out online and submitted via automated email. Similarly, an email form should be linked from the Contact page. I have a logo and business cards designed by ArtQuarry, and I would like the site to have a consistent color scheme and style. The key to design will be to express the joy and love associated with flowers and floral bouquets.
IMPORTANT - I will be exporting the website design to Wordpress CMS in a site hosted by HostNimbus. For smooth integration into WordPress hosted by HostNimbus, the designer should build the site using a WordPress-friendly format. Ideally, they should use HTML, CSS, and PHP. Creating a custom theme or using a page builder that exports to WordPress-compatible files is best. This ensures the site can be easily imported and managed within WordPress.

Target Market(s)

Potential franchisees (existing florists or creative types who might like to own a floral business) and supermarkets who might want us to run their floral department

Industry/Entity Type

Floral retailing

Requirements
Must have
• A brand theme that is beautiful, consistent throughout and builds on the logo design
Nice to have
• Show gender and ethnic diversity in customers and florists. Pictures of happy florists (for franchisees) and pictures of amazing floral department displays (for supermarkets)

```html
<!DOCTYPE html>
<html lang="en">
<head>
<meta charset="utf-8">
<title>Sparrowgate Petals – Supermarket</title>
<link rel="stylesheet" href="https://fonts.googleapis.com/css2?family=Libre+Baskerville:wght@400;700&family=Montserrat:wght@400;500;700&display=swap">
<style>
:root{
  --orange:#f0a024;
  --gold:#f3b02e;
  --green:#14924a;
  --deep-green:#0a7a3e;
  --ink:#111;
  --paper:#fff;
  --soft:#f6f6f6;
}
*{box-sizing:border-box;margin:0;padding:0}
html,body{width:1200px;height:2637px;overflow:hidden;background:var(--paper)}
body{position:relative;font-family:"Montserrat",sans-serif;color:var(--ink)}
.abs{position:absolute}
.serif{font-family:"Libre Baskerville",serif}

.site-header{left:0;top:0;width:1200px;height:92px;background:var(--paper)}
.brand{display:flex;align-items:center;gap:8px;font-family:"Libre Baskerville",serif;font-size:17px;color:var(--orange)}
.brand-dot{width:14px;height:14px;border-radius:50%;background:var(--green)}
.site-header .brand{position:absolute;left:108px;top:34px}
.menu-toggle{left:1050px;top:33px;width:34px;height:22px;display:flex;flex-direction:column;justify-content:space-between}
.menu-toggle span{height:3px;background:var(--ink);display:block}

.hero{left:0;top:92px;width:1200px;height:431px;
  background:radial-gradient(ellipse 360px 200px at 600px 230px,#eef2f2 0 60%,transparent 100%),
  linear-gradient(90deg,#5c4230,#8b6a50 20%,#c9a78f 40%,#b98a6c 75%,#5b4334)}
.hero-mark{left:0;top:353px;width:1200px;text-align:center;font-weight:700;font-size:13px;color:var(--green);letter-spacing:.3px}
.hero-title{left:0;top:372px;width:1200px;text-align:center;font-size:42px;color:var(--ink)}

.ring{border-radius:50%;border:16px solid var(--orange)}
.ring.green{border-color:var(--green)}
.photo{background:linear-gradient(160deg,#cfd6c4,#7d9a78 55%,#3f5a40)}
.ring .photo{width:100%;height:100%;border-radius:50%}
.ornament{background:var(--orange);opacity:.9}

.intro-copy{left:613px;top:755px;width:385px;font-size:12.4px;line-height:19.5px}
.leaf-deco{left:1070px;top:598px;width:130px;height:260px;background:linear-gradient(135deg,transparent 40%,var(--green) 41% 55%,transparent 56%);opacity:.9}

.opportunity{left:0;top:1095px;width:1200px;height:348px;background:var(--soft)}
.opp-photo{left:573px;top:1034px;width:627px;height:409px;
  background:linear-gradient(90deg,rgba(246,246,246,1),rgba(235,230,222,.6) 15%,#d9c6b2 45%,#a8653a 70%,#3d3028)}
.opp-title{left:106px;top:1126px;font-size:29px;font-weight:700}
.opp-list{left:106px;top:1180px;width:385px;list-style:none;font-size:12.6px;line-height:16px}
.opp-list li{position:relative;padding-left:15px;margin-bottom:11px}
.opp-list li::before{content:"";position:absolute;left:0;top:5px;width:7px;height:7px;border-radius:50%;background:var(--orange)}

.partner-copy{left:629px;top:1676px;width:415px;font-size:12.6px;line-height:22.3px}
.flower-deco{left:1050px;top:1555px;width:150px;height:460px;border-radius:80px 0 0 80px;background:linear-gradient(180deg,#f7a21c,#f28a12 50%,#f5b236)}

.contact-card{left:105px;top:2215px;width:978px;height:191px;background:var(--gold)}
.bouquet{left:164px;top:2099px;width:348px;height:307px;border-radius:50% 50% 12% 12%;background:radial-gradient(circle at 50% 35%,#e06aa4,#8d3fa0 45%,#7db64a 75%,#cfe5d2)}
.contact-text{left:539px;top:2283px;font-size:25px;font-weight:700;line-height:27px;color:var(--paper)}
.contact-text a{color:#2a37c8;text-decoration:underline}

.site-footer{left:0;top:2391px;width:1200px;height:246px;background:var(--deep-green)}
.site-footer .brand{position:absolute;left:0;width:1200px;top:80px;justify-content:center;color:var(--paper);font-size:24px}
.site-footer .brand-dot{background:var(--paper)}
.social{left:530px;top:148px;display:flex;gap:8px}
.social span{width:29px;height:29px;border-radius:50%;background:rgba(255,255,255,.22)}
.footer-rule{left:185px;top:205px;width:845px;height:1px;background:rgba(255,255,255,.25)}
.legal{top:220px;font-size:11px;color:var(--paper)}
</style>
</head>
<body>
<header class="site-header abs">
  <div class="brand"><span class="brand-dot"></span>Sparrowgate Petals</div>
  <div class="menu-toggle abs"><span></span><span></span><span></span></div>
</header>

<section class="hero abs" role="img" aria-label="Flat-lay of tulips, peonies and florist scissors on a wooden table around a sheet of white paper"></section>
<div class="hero-mark abs">SPARROWGATE PETALS</div>
<h1 class="hero-title abs serif">Supermarket</h1>

<div class="ornament abs" style="left:82px;top:635px;width:160px;height:155px;border-radius:24px" role="img" aria-label="Orange honeycomb ornament"></div>
<div class="ring abs" style="left:155px;top:637px;width:416px;height:416px">
  <div class="photo" role="img" aria-label="Smiling florist in a green apron holding a bouquet of white flowers"></div>
</div>
<div class="leaf-deco abs" role="img" aria-label="Green leaf stem decoration"></div>
<p class="intro-copy abs">Sparrowgate Petals works with some of the country’s largest and most progressive supermarkets to provide franchisee ownership and operation of their strategically important floral departments.  Supermarkets find that Sparrowgate Petals is able to improve their financial outcomes, provide attentive customer service and satisfaction, and lift the quality of the entire store environment.</p>

<section class="opportunity abs"></section>
<div class="opp-photo abs" role="img" aria-label="Florist in an orange shirt smelling a large arrangement of chrysanthemums"></div>
<h2 class="opp-title abs serif">Opportunity for Supermarkets</h2>
<ul class="opp-list abs">
  <li>Enhance floral revenue streams with efficient assortments and new offerings</li>
  <li>Improve the quality, useful life and merchandising of floral products</li>
  <li>Provide attentive customer service, including semi-custom bouquets, by professional florist staff</li>
  <li>Maintain a beautiful, fresh and well-stocked environment</li>
  <li>Increase sales and profits</li>
  <li>Enhance the entire customer shopping environment</li>
  <li>Reduce the costs of operating a floral department</li>
</ul>

<div class="ornament abs" style="left:0;top:1758px;width:142px;height:260px;border-radius:0 28px 28px 0" role="img" aria-label="Orange honeycomb ornament"></div>
<div class="ring green abs" style="left:155px;top:1630px;width:416px;height:416px">
  <div class="photo" style="background:linear-gradient(160deg,#e6e2dc,#f08fa8 55%,#8f3d86)" role="img" aria-label="Smiling florist in a pink shirt arranging purple and pink flowers"></div>
</div>
<div class="flower-deco abs" role="img" aria-label="Orange gerbera daisies decoration"></div>
<p class="partner-copy abs">Sparrowgate Petals operates in partnership with Frostpine Group, a leading international, multi-channel Japanese food business and the largest franchisor of sushi stations and pre-packaged fruit and vegetable departments to supermarkets across the United States, Canada and the United Kingdom.  Frostpine, working closely with its supermarket partners, has recognised that franchising sushi kiosks and select other supermarket food departments can dramatically improve financial performance for the supermarkets while creating entrepreneurial business opportunities for franchisees.  It has chosen to support Sparrowgate Petals in assisting supermarkets with a similarly compelling opportunity in floral departments.  Sparrowgate Petals’ combination of floral industry experience and supermarket franchising expertise guarantees that consumers, franchisees and supermarket partners each receive exceptional service and value.</p>

<footer class="site-footer abs">
  <div class="brand"><span class="brand-dot"></span>Sparrowgate Petals</div>
  <div class="social abs"><span></span><span></span><span></span><span></span></div>
  <div class="footer-rule abs"></div>
  <p class="legal abs" style="left:185px">© 2024 Sparrowgate Petals, All rights reserved</p>
  <p class="legal abs" style="left:820px">Terms &amp; conditions</p>
  <p class="legal abs" style="left:957px">Privacy policy</p>
</footer>

<div class="contact-card abs"></div>
<div class="bouquet abs" role="img" aria-label="Bouquet of lilies, roses and chrysanthemums in a glass vase"></div>
<p class="contact-text abs serif">For questions and further information,<br>contact <a href="mailto:info@Sparrowgate-Petals.com">info@Sparrowgate-Petals.com</a></p>
</body>
</html>
```